Upmarket Bathroom and Kitchen ware supplier needs a classy business card design

We are a company based in Fiji, we sell plumbing ware (Kitchen and bathroom taps, Basins,showers, toilets etc) through up market show rooms to individuals and directly through Architects and designers of resorts and holiday houses for new builds and renovations. we are wanting to upgrade our over all look and brand. we are starting with a new logo but will be rebranding the whole business. This project is for a business card design for my management and tales team I would like it to be dark, classy and interesting

Target Market(s)

Resort directors and Management, High end holiday home owners

Contact Information for Business Card

Neil Dawson
Director
+64219473815

Colors

Designer to choose colors to be used in the design.

Requirements
Must have
• Must have an upmarket appearance I like darker charcoal shades but will be guided by the designers
• Please any catch phrases like "Crafting remarkable living rooms" this belongs tpo one of our suppliers so can not be used.
Nice to have
• Double sided, so front dedicated to logo provided and back info about the business and the person.

```html
<!DOCTYPE html>
<html lang="en">
<head>
<meta charset="utf-8">
<title>Lagoon Interiors – Business Card</title>
<link href="https://fonts.googleapis.com/css2?family=Arimo:wght@400;500&display=swap" rel="stylesheet">
<style>
  :root{
    --stage:#353892;
    --card:#ffffff;
    --ink:#231f20;
    --text:#2b2b2b;
    --accent:#3a46a0;
    --icon:#3a3f96;
    --pale:#d3e3f5;
    --mid:#a4b6e0;
    --cyan:#7fd1f4;
    --violet:#7684c4;
    --rule:#8a8a8a;
  }
  *{margin:0;padding:0;box-sizing:border-box}
  html,body{width:1200px;height:1000px;overflow:hidden}
  body{background:var(--stage);font-family:"Arimo",Arial,sans-serif;position:relative}
  .card{position:absolute;background:var(--card);overflow:hidden}
  .card-front{left:79px;top:38px;width:779px;height:433px}
  .card-back{left:310px;top:501px;width:807px;height:461px}

  .corner-accent{position:absolute}
  .corner-accent.top-right{top:0;right:0;clip-path:polygon(0 0,100% 0,100% 100%);background:linear-gradient(225deg,var(--mid),var(--pale))}
  .corner-accent.bottom-left{bottom:0;left:0;clip-path:polygon(0 0,100% 100%,0 100%);background:linear-gradient(45deg,var(--violet),var(--cyan))}
  .card-front .corner-accent.top-right{width:200px;height:170px}
  .card-front .corner-accent.bottom-left{width:170px;height:180px}
  .card-back .corner-accent.top-right{width:215px;height:180px}
  .card-back .corner-accent.bottom-left{width:185px;height:210px}

  .brand{position:absolute;text-align:center;color:var(--ink)}
  .brand-dot{position:absolute;border:3px solid var(--ink);border-radius:50%}
  .brand-name{position:absolute;left:0;right:0;font-weight:400;letter-spacing:.42em;line-height:1;white-space:nowrap}
  .brand-rule{position:absolute;height:1px;background:var(--rule)}
  .brand-sub{position:absolute;left:0;right:0;font-weight:400;letter-spacing:.55em;line-height:1;white-space:nowrap}

  .card-front .brand{left:226px;top:120px;width:326px;height:260px}
  .card-front .brand-dot{left:113px;top:15px;width:100px;height:100px}
  .card-front .brand-name{top:178px;font-size:40px;padding-left:.42em}
  .card-front .brand-rule{left:38px;width:250px;top:230px}
  .card-front .brand-sub{top:241px;font-size:15px;padding-left:.55em}

  .card-back .brand{left:94px;top:150px;width:202px;height:190px}
  .card-back .brand-dot{left:61px;top:18px;width:80px;height:80px;border-width:2.5px}
  .card-back .brand-name{top:125px;font-size:30px;padding-left:.42em}
  .card-back .brand-rule{left:20px;width:162px;top:164px}
  .card-back .brand-sub{top:171px;font-size:11px;padding-left:.55em}

  .person{position:absolute;left:59px;top:62px}
  .person-name{font-size:29px;font-weight:400;color:var(--accent);line-height:1.1}
  .person-role{font-size:18px;color:var(--text);letter-spacing:.03em;margin-top:2px}

  .contact{position:absolute;left:418px;top:226px;list-style:none;color:var(--text);font-size:18px}
  .contact li{display:flex;align-items:flex-start;height:39px}
  .contact li.address{line-height:23px}
  .contact svg{width:20px;height:20px;flex:none;margin-right:12px;margin-top:1px;fill:var(--icon)}
</style>
</head>
<body>

<section class="card card-front" aria-label="Card front">
  <div class="corner-accent top-right" role="img" aria-label="Soft blue geometric corner accent"></div>
  <div class="corner-accent bottom-left" role="img" aria-label="Cyan and violet geometric corner accent"></div>
  <div class="brand">
    <span class="brand-dot"></span>
    <span class="brand-name">LAGOON</span>
    <span class="brand-rule"></span>
    <span class="brand-sub">INTERIORS</span>
  </div>
</section>

<section class="card card-back" aria-label="Card back">
  <div class="corner-accent top-right" role="img" aria-label="Soft blue geometric corner accent"></div>
  <div class="corner-accent bottom-left" role="img" aria-label="Cyan and violet geometric corner accent"></div>

  <div class="person">
    <h1 class="person-name">Neil Dawson</h1>
    <p class="person-role">Director</p>
  </div>

  <div class="brand">
    <span class="brand-dot"></span>
    <span class="brand-name">LAGOON</span>
    <span class="brand-rule"></span>
    <span class="brand-sub">INTERIORS</span>
  </div>

  <ul class="contact">
    <li>
      <svg viewBox="0 0 24 24"><path d="M6.6 10.8a15.1 15.1 0 0 0 6.6 6.6l2.2-2.2a1 1 0 0 1 1-.25 11.4 11.4 0 0 0 3.6.57 1 1 0 0 1 1 1V20a1 1 0 0 1-1 1A17 17 0 0 1 3 4a1 1 0 0 1 1-1h3.5a1 1 0 0 1 1 1c0 1.25.2 2.45.57 3.57a1 1 0 0 1-.25 1z"/></svg>
      <span>+64219473815</span>
    </li>
    <li>
      <svg viewBox="0 0 24 24"><path d="M3 9l9 6 9-6v11H3z M3 7.5 12 2l9 5.5-9 6z"/></svg>
      <span>mail@company.com</span>
    </li>
    <li>
      <svg viewBox="0 0 24 24"><path d="M12 2a10 10 0 1 0 0 20 10 10 0 0 0 0-20zm6.9 6h-3a15 15 0 0 0-1.3-3.9A8 8 0 0 1 18.9 8zM12 4c.9 1.2 1.6 2.6 2 4h-4c.4-1.4 1.1-2.8 2-4zM4.3 14a8 8 0 0 1 0-4h3.4a16 16 0 0 0 0 4zm.8 2h3a15 15 0 0 0 1.3 3.9A8 8 0 0 1 5.1 16zm3-8h-3a8 8 0 0 1 4.3-3.9A15 15 0 0 0 8.1 8zM12 20c-.9-1.2-1.6-2.6-2-4h4c-.4 1.4-1.1 2.8-2 4zm2.3-6H9.7a14 14 0 0 1 0-4h4.6a14 14 0 0 1 0 4zm.3 5.9A15 15 0 0 0 15.9 16h3a8 8 0 0 1-4.3 3.9zM16.3 14a16 16 0 0 0 0-4h3.4a8 8 0 0 1 0 4z"/></svg>
      <span>www.company.com</span>
    </li>
    <li class="address">
      <svg viewBox="0 0 24 24"><path d="M12 2a7 7 0 0 0-7 7c0 5.2 7 13 7 13s7-7.8 7-13a7 7 0 0 0-7-7zm0 9.5A2.5 2.5 0 1 1 12 6.5a2.5 2.5 0 0 1 0 5z"/></svg>
      <span>Lagoon Interiors<br>48 Coral Street, Lautoka, Fiji.</span>
    </li>
  </ul>
</section>

</body>
</html>
```